VMR business card

Need a business card for a company that provides instructional design and elearning development services. The website is here: http://vantmoro.studio/

I'm attaching a current logo, as well as the old business card design. While I like to keep it clean, the old design is too simplistic for my liking. The only idea I want to reuse from the old design is placing industry jargon on the back of the card, just need a better way to present it. But if you have other ideas for the back--feel free to experiment.

Please use the colors complementary to the color we have on the website. Thank you!

```html
<!DOCTYPE html>
<html lang="en">
<head>
<meta charset="utf-8">
<title>VMR Business Card</title>
<link href="https://fonts.googleapis.com/css2?family=Open+Sans:ital,wght@0,400;0,600;0,700;1,400&family=Righteous&display=swap" rel="stylesheet">
<style>
  :root {
    --page-bg: #e9e6e1;
    --card-black: #0b0b0b;
    --card-white: #ffffff;
    --teal: #2ab3a6;
    --teal-dark: #1f8f86;
    --gold: #e4d68f;
    --ink: #2a2a2a;
    --grey-strip: #5c5c5c;
    --grey-light: #8a8a8a;
  }
  * { box-sizing: border-box; margin: 0; padding: 0; }
  html, body {
    width: 1200px; height: 900px; overflow: hidden;
    background: var(--page-bg);
  }
  .sheet {
    width: 1200px; height: 900px;
    display: flex; flex-direction: column; align-items: center; justify-content: center;
    gap: 40px;
  }
  .card {
    width: 680px; height: 389px;
    position: relative; overflow: hidden;
    box-shadow: 0 10px 28px rgba(0,0,0,.22);
  }

  /* Back */
  .card-back { background: var(--card-black); padding: 42px 48px; }
  .help-title {
    font-family: "Righteous", sans-serif;
    font-size: 50px; letter-spacing: 2px; line-height: 1;
    background: linear-gradient(90deg, var(--teal) 0%, var(--gold) 100%);
    -webkit-background-clip: text; background-clip: text; color: transparent;
    margin-bottom: 22px;
  }
  .service-list { list-style: none; font-family: "Righteous", sans-serif; font-size: 25px; letter-spacing: 1.5px; line-height: 1.3; }
  .service-list li { display: flex; align-items: center; gap: 16px; text-transform: uppercase; }
  .service-list li::before { content: ""; width: 8px; height: 8px; border-radius: 50%; background: currentColor; }
  .service-list li:nth-child(1) { color: var(--gold); }
  .service-list li:nth-child(2) { color: #c2d092; }
  .service-list li:nth-child(3) { color: #92c79b; }
  .service-list li:nth-child(4) { color: #5cbda2; }
  .service-list li:nth-child(5) { color: var(--teal); }
  .service-list li:nth-child(6) { color: var(--teal); }
  .back-brand {
    position: absolute; right: 44px; top: 150px;
    display: flex; align-items: center; gap: 8px;
    font-family: "Open Sans", sans-serif; font-weight: 700; font-size: 22px; color: var(--teal);
  }
  .back-brand .mark { width: 12px; height: 12px; background: var(--teal); }

  /* Front */
  .card-front { background: var(--card-white); }
  .front-brand {
    height: 150px; display: flex; align-items: center; justify-content: center;
    font-family: "Open Sans", sans-serif; font-weight: 700; font-size: 72px; letter-spacing: 4px; color: var(--teal);
  }
  .name-band {
    height: 62px; background: var(--card-black);
    border-top: 3px solid var(--teal); border-bottom: 3px solid var(--teal);
    display: flex; align-items: center; justify-content: center;
    font-family: "Open Sans", sans-serif; font-weight: 700; font-size: 20px; color: #fff; letter-spacing: .5px;
  }
  .contact-list {
    list-style: none; padding: 22px 0 0 46px;
    font-family: "Open Sans", sans-serif; font-style: italic; font-size: 19px; color: var(--ink); line-height: 1.45;
  }
  .contact-list li { display: flex; align-items: center; gap: 12px; }
  .contact-list svg { width: 16px; height: 16px; fill: none; stroke: var(--ink); stroke-width: 2; }
  .base-strip { position: absolute; left: 0; right: 0; bottom: 0; height: 28px; display: flex; }
  .base-strip .strip-black { flex: 1; background: var(--card-black); }
  .base-strip .strip-grey { width: 190px; background: var(--grey-strip); }
  .base-strip .strip-light { width: 40px; background: var(--grey-light); }
</style>
</head>
<body>
<main class="sheet">
  <section class="card card-back" aria-label="Card back">
    <h2 class="help-title">HOW CAN WE HELP?</h2>
    <ul class="service-list">
      <li>Mobile Learning SCORM</li>
      <li>Instructional Design LMS</li>
      <li>MOOCs eLearning HTML5</li>
      <li>Adult Learning Theory</li>
      <li>Gamification Classroom</li>
      <li>xAPI Blended Learning</li>
    </ul>
    <div class="back-brand"><span class="mark"></span>VMR</div>
  </section>

  <section class="card card-front" aria-label="Card front">
    <div class="front-brand">VMR</div>
    <div class="name-band">Darren Keplow</div>
    <ul class="contact-list">
      <li>
        <svg viewBox="0 0 16 16"><path d="M4 2 L6.5 2 L7.5 5 L6 6.5 Q7.5 9.5 9.5 10 L11 8.5 L14 9.5 L14 12 Q13 14 11 14 Q3 12 2 4 Q2 2 4 2 Z"/></svg>
        555-013-4827
      </li>
      <li>
        <svg viewBox="0 0 16 16"><rect x="1.5" y="3.5" width="13" height="9"/><path d="M1.5 3.5 L8 9 L14.5 3.5"/></svg>
        dkeplow@vantmoro.studio
      </li>
      <li>
        <svg viewBox="0 0 16 16"><circle cx="8" cy="8" r="6.5"/><ellipse cx="8" cy="8" rx="3" ry="6.5"/><path d="M1.5 8 H14.5"/></svg>
        www.vantmoro.studio
      </li>
    </ul>
    <div class="base-strip"><span class="strip-black"></span><span class="strip-grey"></span><span class="strip-light"></span></div>
  </section>
</main>
</body>
</html>
```